End of the Year Postcard

Bright Harbor Allies - a non profit addressing peace and justice issues from an interfaith perspective

Industry/Entity Type

Non Profit

```html
<!DOCTYPE html>
<html lang="en">
<head>
<meta charset="utf-8">
<title>Bright Harbor Allies – End of Year Postcard</title>
<link href="https://fonts.googleapis.com/css2?family=Source+Sans+3:wght@400;600;700&family=Signika:wght@700&family=Alegreya+SC:wght@700&display=swap" rel="stylesheet">
<style>
  :root {
    --bg: #9a9a9a;
    --blue: #0b6fb6;
    --blue-deep: #0a5e9e;
    --white: #ffffff;
    --orange: #f5a21b;
    --rule: #a8a8a8;
    --ink: #333333;
  }
  * { box-sizing: border-box; margin: 0; padding: 0; }
  html, body { width: 911px; height: 1200px; overflow: hidden; background: var(--bg); font-family: "Source Sans 3", sans-serif; }
  .card { position: absolute; left: 48px; width: 806px; height: 537px; background: var(--white); overflow: hidden; box-shadow: 0 4px 14px rgba(0,0,0,.35); }
  .card--front { top: 37px; }
  .card--back { top: 629px; }
  .photo { position: absolute; }
  .band { position: absolute; left: 0; top: 173px; width: 806px; height: 198px; background: var(--blue); }
  .inset { position: absolute; left: 68px; top: 146px; width: 236px; height: 161px; background: var(--white); padding: 6px; transform: rotate(-2deg); box-shadow: 0 2px 6px rgba(0,0,0,.4); }
  .inset .photo { position: static; width: 100%; height: 100%; }
  .site { position: absolute; left: 72px; top: 325px; color: var(--white); font-size: 17px; letter-spacing: 1px; }
  .highlights { position: absolute; left: 338px; top: 170px; width: 394px; height: 196px; border: 1.5px dashed var(--white); border-top: none; }
  .highlights__inner { position: absolute; left: 12px; top: 4px; transform: rotate(-3.2deg); transform-origin: left top; color: var(--white); }
  .highlights h2 { font-weight: 400; font-size: 27px; margin-bottom: 4px; }
  .highlights li { list-style: none; font-size: 13.5px; line-height: 1.6; padding-left: 12px; position: relative; }
  .highlights li::before { content: ""; position: absolute; left: 0; top: 8px; width: 5px; height: 5px; background: var(--orange); }
  .highlights li span { display: block; line-height: 1.2; }
  .connectors { position: absolute; left: 0; top: 0; }

  .back__band { position: absolute; left: 0; top: 0; width: 562px; height: 106px; background: var(--blue); color: var(--white); text-align: center; padding-top: 26px; }
  .back__band p { font-size: 12.6px; line-height: 1.5; }
  .back__band strong { display: block; font-size: 24px; font-weight: 700; margin-top: 2px; }
  .brand { position: absolute; left: 568px; top: 44px; display: flex; align-items: center; gap: 6px; color: var(--blue-deep); font-family: "Source Sans 3", sans-serif; font-weight: 600; font-size: 17px; line-height: 1; width: 130px; }
  .brand__dot { width: 26px; height: 26px; border-radius: 50%; background: var(--blue-deep); flex: none; }
  .stamp { position: absolute; left: 702px; top: 14px; width: 88px; height: 120px; border: 1px solid var(--rule); }
  .address-line { position: absolute; left: 572px; width: 208px; height: 1px; background: var(--rule); }
  .join { position: absolute; left: 0; width: 562px; text-align: center; color: var(--blue); }
  .join__title { top: 110px; font-family: "Signika", sans-serif; font-size: 38px; }
  .join__sub { top: 155px; font-size: 17px; }
  .crowd { position: absolute; left: 72px; top: 180px; width: 400px; height: 128px; }
  .headline { position: absolute; left: 0; top: 290px; width: 562px; text-align: center; color: var(--blue); font-family: "Alegreya SC", serif; font-size: 38px; line-height: 0.95; letter-spacing: -1px; }
  .send { position: absolute; left: 320px; top: 392px; color: var(--blue); font-size: 14.5px; }
  .strip { position: absolute; left: 0; top: 414px; width: 28px; height: 67px; background: var(--blue); }
  .partner { position: absolute; }
  .partner--a { left: 42px; top: 414px; width: 78px; height: 55px; background: #3b66b0; }
  .partner--b { left: 132px; top: 420px; width: 90px; height: 48px; background: #7cc6ec; }
  .partner--c { left: 232px; top: 413px; width: 66px; height: 66px; border-radius: 50%; background: #5b5650; border: 3px solid #c7c2b8; }
  .sendto { position: absolute; left: 304px; top: 414px; width: 256px; height: 67px; background: var(--blue); color: var(--white); text-align: center; padding-top: 3px; }
  .sendto h3 { font-size: 20px; font-weight: 700; line-height: 1.1; }
  .sendto p { font-size: 11.5px; line-height: 1.35; }
</style>
</head>
<body>

<section class="card card--front">
  <div class="photo" role="img" aria-label="Group photo of youth leaders indoors" style="left:0;top:0;width:286px;height:173px;background:linear-gradient(#6b5e58,#3e3b45);"></div>
  <div class="photo" role="img" aria-label="Students on the steps of a pink stone temple" style="left:288px;top:0;width:272px;height:173px;background:linear-gradient(#6fa6d8,#c99b8f 45%,#8a6f6b);"></div>
  <div class="photo" role="img" aria-label="Students on a rooftop with a city skyline" style="left:562px;top:0;width:244px;height:173px;background:linear-gradient(#aac9ea,#8d8b8e 60%,#4e4a4d);"></div>

  <div class="band"></div>

  <div class="inset"><div class="photo" role="img" aria-label="Film festival winners holding certificates" style="background:linear-gradient(#7a3a2c,#5a4040);"></div></div>

  <p class="site">www.brightharborallies.org</p>

  <div class="highlights">
    <div class="highlights__inner">
      <h2>Highlights from 2015</h2>
      <ul>
        <li>3 Interfaith Youth Leadership Initiatives<span>(Westfield University, Cardinal College, Bayview State)</span></li>
        <li>IYCHC – Interfaith Youth Council of Harbor County</li>
        <li>IYCSC – Interfaith Youth Council of Summit County</li>
        <li>Student Interfaith Film Festival</li>
        <li>Student Leadership Trip to Washington DC</li>
        <li>Abrahamic Faiths Peacemaking Initiative</li>
      </ul>
    </div>
  </div>

  <div class="photo" role="img" aria-label="Students at a war memorial statue in Washington DC" style="left:0;top:371px;width:243px;height:166px;background:linear-gradient(#5a9ad8,#5d6a55 60%,#3a3a3a);"></div>
  <div class="photo" role="img" aria-label="Students beside a city limit street sign" style="left:245px;top:371px;width:232px;height:166px;background:linear-gradient(#9a988e,#2f5b3a 45%,#6d6863);"></div>
  <div class="photo" role="img" aria-label="Volunteers at a food bank warehouse" style="left:478px;top:371px;width:328px;height:166px;background:linear-gradient(#8b7561,#b0a99e 50%,#5a5552);"></div>

  <svg class="connectors" width="806" height="537" viewBox="0 0 806 537" aria-hidden="true">
    <defs><marker id="arrow" markerWidth="8" markerHeight="8" refX="6" refY="4" orient="auto"><path d="M0 0 L8 4 L0 8 z" fill="#fff"/></marker></defs>
    <path d="M350 210 C320 200 310 180 312 160" stroke="#fff" stroke-width="1.2" fill="none" marker-end="url(#arrow)"/>
    <path d="M348 316 C330 310 300 300 270 296" stroke="#fff" stroke-width="1.2" fill="none"/>
    <path d="M350 346 C280 380 220 410 158 448" stroke="#fff" stroke-width="1.2" fill="none" marker-end="url(#arrow)"/>
    <path d="M216 394 L338 368" stroke="#fff" stroke-width="1.5" stroke-dasharray="5 4" fill="none"/>
  </svg>
</section>

<section class="card card--back">
  <div class="back__band">
    <p>In light of recent world events, our goals of interfaith cooperation, leadership development<br>and community service are needed now more than ever. To donate GO TO PAYWELL, AND GIVE TO</p>
    <strong>donate@brightharborallies.org</strong>
  </div>

  <div class="brand"><span>Bright Harbor Allies</span><span class="brand__dot"></span></div>
  <div class="stamp"></div>
  <div class="address-line" style="top:218px"></div>
  <div class="address-line" style="top:255px"></div>
  <div class="address-line" style="top:293px"></div>
  <div class="address-line" style="top:331px"></div>
  <div class="address-line" style="top:369px"></div>

  <h1 class="join join__title">Please join</h1>
  <p class="join join__sub">Bright Harbor Allies in our campaign to develop</p>
  <div class="crowd" role="img" aria-label="Crowd of people forming two hands shaping a heart" style="background:radial-gradient(ellipse at 50% 70%,#6b6a58 0%,#8d7d62 40%,rgba(255,255,255,0) 72%);"></div>
  <h2 class="headline">The Next<br>Generation of Multi-Faith<br>Leaders!</h2>

  <p class="send">Or send your donation directly to</p>
  <div class="strip"></div>
  <div class="partner partner--a" role="img" aria-label="Partner youth council badge"></div>
  <div class="partner partner--b" role="img" aria-label="Partner leadership initiative badge"></div>
  <div class="partner partner--c" role="img" aria-label="Partner youth council seal"></div>
  <div class="sendto">
    <h3>Bright Harbor Allies</h3>
    <p>418 Lantern Way, Alder Bay, CA 90210<br>(555) 014-2290, www.brightharborallies.org</p>
  </div>
</section>

</body>
</html>
```